Website Design for LipoweZacisze.pl – Luxury Wedding Car Rental with Chauffeur

We are looking for a talented designer to create a modern, elegant, and fully responsive website for our new brand – LipowyZacisze.pl. We are a premium car rental platform in Poland, offering luxury and exotic vehicles exclusively for weddings. All cars come with a professional chauffeur, ensuring a high-end, stress-free, and stylish experience.
Website Purpose:
The website should present our offering in a luxurious, clear, and inspiring way. It must build trust, highlight the prestige of our brand, and encourage inquiries. Our target audience includes engaged couples, wedding planners, and clients seeking a truly exceptional vehicle for their special day.
Design Requirements:
Style: modern, elegant, minimalist
Color palette: white, black, gold, optionally silver – refined and luxurious
Typography: clean, modern, high-end
Layout: clear, intuitive, with large car images and well-defined sections
Fully responsive (desktop, tablet, mobile)
Bilingual layout (Polish/English) must be considered
Pages to Design:
Homepage
About Us
Fleet Overview
Individual Car Pages
Services (Weddings, Photo Shoots, Film Rentals)
Why Us / Unique Selling Points
Contact
FAQ
Inspiration:
Luxury automotive brands (e.g. Vellor-Kane, Carrow, Dunmere Vale)
High-end wedding websites
Minimalist layouts with large visuals and elegant typography
Additional Notes:
The design should evoke the emotions of a wedding day – elegance, uniqueness, style, and class. Please avoid flashy colors, excessive graphic effects, or overly decorative elements. Subtlety, prestige, and sophistication are key.

```html
<!DOCTYPE html>
<html lang="pl">
<head>
<meta charset="UTF-8">
<title>LipoweZacisze.pl – Przejazdy ślubne</title>
<link rel="stylesheet" href="https://fonts.googleapis.com/css2?family=Great+Vibes&family=Marcellus&family=Montserrat:wght@400;500&family=Cormorant+Garamond:wght@500&display=swap">
<style>
  :root{
    --gold:#e6cb6a;
    --gold-line:#cdb05a;
    --gold-text:#b8954a;
    --ink:#121212;
    --hero-bg:#05080b;
    --band-bg:#0b121a;
    --paper:#ffffff;
    --muted-light:#c9c9c9;
    --muted-dark:#5c4a34;
  }
  *{margin:0;padding:0;box-sizing:border-box}
  html,body{width:800px;height:1200px;overflow:hidden;background:var(--paper)}
  body{position:relative;font-family:"Montserrat",sans-serif}
  h1,h2{font-weight:400}

  .site-header{position:absolute;left:0;top:0;width:800px;height:68px;background:var(--paper)}
  .brand{position:absolute;left:60px;top:21px;display:flex;align-items:center;gap:8px;
    font-family:"Cormorant Garamond",serif;font-weight:500;font-size:20px;color:var(--ink)}
  .brand-dot{width:20px;height:20px;border:1.5px solid var(--gold-line);border-radius:50%}
  .main-nav{position:absolute;left:290px;top:28px;display:flex;gap:16px;
    font-family:"Marcellus",serif;font-size:9px;letter-spacing:.3px;color:var(--ink)}
  .main-nav .active{color:#6b4e22;border-bottom:1px solid var(--gold-line);padding-bottom:3px}
  .header-cta{position:absolute;left:617px;top:15px;width:102px;height:38px;border:1.5px solid var(--gold-line);
    display:flex;align-items:center;justify-content:center;font-family:"Marcellus",serif;font-size:8.5px;color:var(--ink)}

  .hero{position:absolute;left:0;top:68px;width:800px;height:438px;background:var(--hero-bg);overflow:hidden}
  .hero-photo{position:absolute;right:0;top:0;width:460px;height:438px;
    background:radial-gradient(ellipse at 62% 48%,#6d6a5c 0%,#3a3a33 35%,#15181a 65%,var(--hero-bg) 92%)}
  .hero-title{position:absolute;left:98px;top:52px;color:var(--gold)}
  .script-sm{font-family:"Great Vibes",cursive;font-weight:400;font-size:62px;line-height:1}
  .hero .script-lg{font-family:"Great Vibes",cursive;font-weight:400;font-size:92px;line-height:1;margin:8px 0 0 -28px}
  .hero-caps{font-family:"Marcellus",serif;font-weight:400;font-size:40px;letter-spacing:5px;margin:2px 0 0 20px}
  .hero-copy{position:absolute;left:88px;top:287px;width:290px;font-size:7.5px;line-height:13px;color:var(--muted-light)}
  .btn{position:absolute;border:1px solid var(--gold-line);display:flex;align-items:center;justify-content:center;
    font-family:"Marcellus",serif;color:var(--gold);letter-spacing:.5px}
  .hero .btn{top:353px;height:35px;font-size:8px}

  .welcome{position:absolute;left:0;top:506px;width:800px;height:395px;background:var(--band-bg);text-align:center;color:var(--gold)}
  .welcome .script-sm{position:absolute;left:0;width:800px;top:52px;font-size:52px}
  .welcome .script-lg{position:absolute;left:0;width:800px;top:100px;font-family:"Great Vibes",cursive;font-weight:400;font-size:84px;line-height:1}
  .welcome-copy{position:absolute;left:180px;top:213px;width:440px;font-size:10px;line-height:15.5px;color:var(--gold-text)}
  .welcome .btn{top:300px;height:41px;font-size:10px}

  .contact{position:absolute;left:0;top:901px;width:800px;height:299px;background:var(--paper);text-align:center}
  .contact h2{position:absolute;left:0;width:800px;top:48px;font-family:"Marcellus",serif;font-size:33px;color:var(--ink);letter-spacing:1px}
  .contact-copy{position:absolute;left:150px;top:112px;width:500px;font-size:10px;line-height:16.5px;color:var(--muted-dark)}
  .contact-phone{position:absolute;left:0;width:800px;top:195px;font-family:"Marcellus",serif;font-size:25px;color:var(--ink)}
</style>
</head>
<body>
  <header class="site-header">
    <div class="brand"><span>LipoweZacisze.pl</span><span class="brand-dot"></span></div>
    <nav class="main-nav">
      <span class="active">HOME</span><span>O NAS</span><span>FLOTA</span><span>USŁUGI</span><span>DLACZEGO MY / FAQ</span>
    </nav>
    <div class="header-cta">SKONTAKTUJ SIĘ</div>
  </header>

  <section class="hero">
    <div class="hero-photo" role="img" aria-label="Luksusowa limuzyna ślubna w ciemnym studiu"></div>
    <h1 class="hero-title">
      <div class="script-sm">Witamy w</div>
      <div class="script-lg">Lipowe</div>
      <div class="hero-caps">ZACISZE</div>
    </h1>
    <p class="hero-copy">Lorem ipsum dolor sit amet, consectetur adipiscing elit. Sed do eiusmod tempor incididunt ut labore et dolore magna aliqua. Ut enim ad minim veniam, quis nostrud exercitation ullamco laboris nisi ut aliquip ex ea commodo consequat.</p>
    <div class="btn" style="left:88px;width:113px">O NAS</div>
    <div class="btn" style="left:227px;width:125px">NASZE USŁUGI</div>
  </section>

  <section class="welcome">
    <div class="script-sm">Witamy w</div>
    <h2 class="script-lg">Lipowe Zacisze</h2>
    <p class="welcome-copy">Lorem ipsum dolor sit amet, consectetur adipiscing elit, sed dolor eiusmod tempor incididunt ut labore et dolore magna aliqua. Duis aute irure dolor in reprehenderit ullamco laboris nisi ut aliquip ex ea commodo.</p>
    <div class="btn" style="left:232px;width:150px">O NAS</div>
    <div class="btn" style="left:418px;width:160px">NASZE USŁUGI</div>
  </section>

  <section class="contact">
    <h2>SKONTAKTUJ SIĘ</h2>
    <p class="contact-copy">Lorem ipsum dolor sit amet, consectetur adipiscing elit, sed do eiusmod tempor, incididunt ut labore et dolore magna aliqua ut enim ad minim veniam, quis nostrud exercitation ullamco laboris nisi ut aliquip ex ea commodo consequat.</p>
    <div class="contact-phone">+00 123 456 789</div>
  </section>
</body>
</html>
```